Computer Company needs a Business card design

We need a business card design for our business. We assist people to transition to the QTG (Quillary Telelink Grid). The Australian Government-owned qtg™ network is a brand new telecommunications network currently being rolled out across Australia, giving access to a reliable broadband connection. Our niche market will predominantly be domestic customers in the 50+ age bracket. The assistance that we provide is everything from arranging the equipment, arranging the plan and contract term, appointment times, final testing of the network and any tweaks that need to be made. We basically PM the transition from start to finish. The business card design should be minimalist, should communicate loyalty and stability, should be easy to read and clearly explain what we do. We have asked for front and back. However, the back of the card does not have to include much information at all. It could be just a small design, or a repeat of our phone number. Up to you. The attached file only says what is required on the card. It does not specify where to arrange the text, what fonts to use, etc etc. As much as we would like to give you more info, due to our very limited design ability, we are not really able to send you any rough, or otherwise, designs of what we are after. Hopefully the above description is enough for you.

```html
<!DOCTYPE html>
<html lang="en">
<head>
<meta charset="utf-8">
<title>Clearpath Connect – Business Card</title>
<link href="https://fonts.googleapis.com/css2?family=Lato:wght@400;700&display=swap" rel="stylesheet">
<style>
  :root {
    --brand-blue: #1d3f9a;
    --brand-blue-deep: #2a3f95;
    --brand-blue-bright: #0a7cc6;
    --swoosh-grey: #c3c4c6;
    --ink: #1a1a1a;
    --paper: #ffffff;
    --backdrop: #e9eaed;
  }
  * { box-sizing: border-box; margin: 0; padding: 0; }
  html, body { width: 1200px; height: 680px; overflow: hidden; }
  body {
    background: var(--backdrop);
    font-family: "Lato", Arial, sans-serif;
    display: flex;
    align-items: center;
    justify-content: center;
    gap: 40px;
  }
  .card {
    position: relative;
    width: 540px;
    height: 308px;
    border-radius: 4px;
    overflow: hidden;
    box-shadow: 0 6px 20px rgba(0,0,0,.15);
  }

  /* Front */
  .card-front { background: var(--paper); }
  .brand-name {
    position: absolute;
    left: 36px;
    top: 50px;
    font-weight: 700;
    font-size: 32px;
    color: var(--brand-blue);
    letter-spacing: .3px;
  }
  .holder-name {
    position: absolute;
    right: 40px;
    top: 62px;
    font-weight: 700;
    font-size: 21px;
    color: var(--brand-blue);
  }
  .divider {
    position: absolute;
    left: 36px;
    right: 40px;
    top: 128px;
    height: 1px;
    background: var(--brand-blue);
  }
  .address {
    position: absolute;
    right: 40px;
    top: 142px;
    text-align: right;
    font-style: normal;
    font-size: 15px;
    line-height: 1.35;
    color: var(--ink);
  }
  .contact-list {
    position: absolute;
    left: 36px;
    top: 150px;
    list-style: none;
    font-size: 17px;
    color: var(--ink);
  }
  .contact-list li {
    display: flex;
    align-items: center;
    gap: 12px;
    margin-bottom: 6px;
  }
  .contact-list svg { width: 16px; height: 16px; fill: var(--brand-blue); flex: none; }
  .swoosh { position: absolute; left: 0; bottom: 0; width: 540px; height: 120px; }
  .front-web {
    position: absolute;
    right: 22px;
    bottom: 12px;
    font-size: 14px;
    color: var(--paper);
  }

  /* Back */
  .card-back {
    background: radial-gradient(circle at 65% 35%, var(--brand-blue-bright) 0%, var(--brand-blue-deep) 75%);
    color: var(--paper);
  }
  .back-name {
    position: absolute;
    left: 0; right: 0;
    top: 112px;
    text-align: center;
    font-weight: 700;
    font-size: 44px;
    color: var(--paper);
  }
  .back-web {
    position: absolute;
    left: 0; right: 0;
    bottom: 48px;
    text-align: center;
    font-size: 16px;
    letter-spacing: .5px;
  }
</style>
</head>
<body>
  <section class="card card-front">
    <p class="brand-name">Clearpath Connect</p>
    <p class="holder-name">Reid Carrow</p>
    <div class="divider"></div>
    <address class="address">2150 Harbor Lane<br>Port Vale TX 78100</address>
    <ul class="contact-list">
      <li>
        <svg viewBox="0 0 24 24" aria-hidden="true"><path d="M6.6 10.8a15.1 15.1 0 0 0 6.6 6.6l2.2-2.2a1 1 0 0 1 1-.25 11.4 11.4 0 0 0 3.6.57 1 1 0 0 1 1 1V20a1 1 0 0 1-1 1A17 17 0 0 1 3 4a1 1 0 0 1 1-1h3.5a1 1 0 0 1 1 1c0 1.25.2 2.450.57 3.57a1 1 0 0 1-.25 1z"/></svg>
        042 581 0937
      </li>
      <li>
        <svg viewBox="0 0 24 24" aria-hidden="true"><path d="M2 5h20v14H2zm2 2v.5l8 5 8-5V7zm0 2.8V17h16V9.8l-8 5z"/></svg>
        info@clearpathconnect.com.au
      </li>
    </ul>
    <svg class="swoosh" viewBox="0 0 540 120" preserveAspectRatio="none" aria-hidden="true">
      <path d="M150 120 C 300 60, 420 40, 540 28 L540 120 Z" fill="var(--swoosh-grey)"/>
      <path d="M210 120 C 330 75, 430 58, 540 50 L540 120 Z" fill="var(--brand-blue)"/>
    </svg>
    <p class="front-web">www.clearpathconnect.com.au</p>
  </section>

  <section class="card card-back">
    <p class="back-name">Clearpath Connect</p>
    <p class="back-web">www.clearpathconnect.com.au</p>
  </section>
</body>
</html>
```